Brochure Redesign

We need a new, adapted, design for our Brochure. A few weeks ago we've setup a new Homepage design and for now we want to adapt our old Brochure to the new design.

Requirements:
-) Place the 3 products quite prominent
-) Place also our add ons
-) Use the Keyvisuals you can find on the Homepage

New Homepage: www.rufwerkstatt.at
Old Folder version - see attached

Requirements
Must have
• Logo and basic design from Homepage

```html
<!DOCTYPE html>
<html lang="de">
<head>
<meta charset="utf-8">
<title>rufwerkstatt.at – Broschüre</title>
<link rel="stylesheet" href="https://fonts.googleapis.com/css2?family=Ubuntu:wght@400;500;700&display=swap">
<style>
  :root {
    --maroon: #6b1512;
    --orange: #f7941d;
    --grey-pie: #6e6e6e;
    --panel: #e4e4e4;
    --hero-bg: #f4f7f9;
    --page: #ffffff;
    --stage: #d4d4d4;
    --text: #333333;
    --muted: #5a5a5a;
  }
  * { box-sizing: border-box; margin: 0; padding: 0; }
  html, body { width: 927px; height: 1200px; overflow: hidden; }
  body {
    background: var(--stage);
    font-family: "Ubuntu", sans-serif;
    color: var(--text);
  }
  .brochure {
    width: 927px;
    height: 662px;
    background: var(--page);
    position: relative;
  }
  /* Header */
  .masthead { height: 80px; position: relative; }
  .brand {
    position: absolute; left: 0; right: 0; top: 26px;
    display: flex; justify-content: center; align-items: center; gap: 8px;
  }
  .brand-name {
    font-size: 24px; font-weight: 500; color: var(--maroon);
  }
  .brand-mark {
    width: 10px; height: 10px; border-radius: 50%; background: var(--maroon);
  }
  .quality-badge {
    position: absolute; right: 42px; top: 16px;
    width: 46px; height: 52px; background: var(--maroon);
  }
  .band-thick { height: 21px; background: var(--maroon); }
  .band-gap { height: 4px; }
  .band-thin { height: 7px; background: var(--maroon); }

  /* Hero */
  .hero {
    height: 187px; background: var(--hero-bg);
    display: flex; position: relative;
  }
  .hero-photo {
    width: 185px; height: 100%; flex: 0 0 185px;
    background: linear-gradient(90deg, #e9d4c4 0%, #f0e4da 55%, #f4f7f9 100%);
  }
  .hero-columns {
    display: flex; padding-top: 28px; padding-left: 8px;
  }
  .feature { width: 177px; padding-right: 10px; }
  .feature h2 {
    font-size: 22px; font-weight: 500; color: var(--maroon);
    line-height: 1.05; letter-spacing: -0.3px;
  }
  .feature h3 {
    font-size: 12.5px; font-weight: 500; color: var(--maroon);
    margin-bottom: 8px; white-space: nowrap;
  }
  .feature p, .feature ul {
    font-size: 9.5px; line-height: 1.65; color: var(--muted); list-style: none;
  }

  /* Section bands */
  .section-band {
    height: 21px; background: var(--maroon); color: #fff;
    text-align: center; font-size: 14px; font-weight: 700;
    letter-spacing: 5px; line-height: 21px;
  }

  /* Products */
  .products {
    display: flex; gap: 14px; padding: 13px 31px 15px;
  }
  .product { width: 279px; }
  .product-title {
    background: var(--orange); color: #fff; font-size: 15px; font-weight: 500;
    height: 23px; line-height: 23px; padding-left: 5px;
    border-radius: 4px 4px 0 0;
  }
  .product-body {
    background: var(--panel); height: 112px; display: flex;
    padding: 10px 8px 0 6px;
  }
  .product-body svg { flex: 0 0 82px; margin-top: 6px; }
  .product-copy { padding-left: 8px; }
  .product-copy h4 { font-size: 10px; font-weight: 700; margin-bottom: 7px; }
  .product-copy p { font-size: 9px; line-height: 1.55; color: var(--muted); }

  /* Add-ons */
  .addons {
    display: flex; gap: 16px; padding: 12px 31px 0;
  }
  .addon { width: 277px; }
  .addon-title {
    background: var(--orange); color: #fff; font-size: 11.5px; font-weight: 500;
    height: 19px; line-height: 19px; text-align: center;
    border-radius: 7px 7px 0 0;
  }
  .addon-body {
    background: var(--panel); height: 95px; padding: 6px 6px;
    font-size: 9px; line-height: 1.55; color: var(--text);
  }
</style>
</head>
<body>
  <main class="brochure">
    <header class="masthead">
      <div class="brand">
        <span class="brand-name">rufwerkstatt.at</span>
        <span class="brand-mark"></span>
      </div>
      <div class="quality-badge" role="img" aria-label="Gütesiegel"></div>
    </header>
    <div class="band-thick"></div>
    <div class="band-gap"></div>
    <div class="band-thin"></div>

    <section class="hero">
      <div class="hero-photo" role="img" aria-label="Foto einer Telefonistin mit Headset"></div>
      <div class="hero-columns">
        <article class="feature">
          <h2>Ihre Vorteile</h2>
          <h3>Einfach, Immer, Erreichbar</h3>
          <ul>
            <li>- Individueller Meldetext</li>
            <li>- Beliebig viele Mitarbeiter</li>
            <li>- 24h Erreichbarkeit</li>
            <li>- Ohne Mindestvertragslaufzeit</li>
            <li>- Keine versteckten Callminuten</li>
          </ul>
        </article>
        <article class="feature">
          <h2>Dateneingabe</h2>
          <h3>Einfach, Immer, Erreichbar</h3>
          <p>Sie können Ihr neues Sekretariat in nur wenigen Minuten ganz einfach online einrichten. Geben Sie alle relevanten Daten menügeführt ein.</p>
        </article>
        <article class="feature">
          <h2>Rufumleitung</h2>
          <h3>Einfach, Immer, Erreichbar</h3>
          <p>Sofort nach erfolgreicher Buchung erhalten Sie Ihre Zielrufnummer. Leiten Sie ihr Telefon einfach auf diese Nummer um</p>
        </article>
        <article class="feature">
          <h2>Ihr Sekretariat</h2>
          <h3>Einfach, Immer, Erreichbar</h3>
          <p>Ihr neues Sekretariat ist nun aktiv. Sie und all Ihre Mitarbeiter werden in Echtzeit, individuell über eingehende Anrufe informiert.</p>
        </article>
      </div>
    </section>

    <div class="section-band">INBOUND</div>

    <svg width="0" height="0" style="position:absolute">
      <defs>
        <radialGradient id="sun" cx="50%" cy="50%" r="50%">
          <stop offset="0%" stop-color="#ffd200"/>
          <stop offset="100%" stop-color="#f29100"/>
        </radialGradient>
      </defs>
    </svg>

    <section class="products">
      <article class="product">
        <div class="product-title">Bürozeiten</div>
        <div class="product-body">
          <svg viewBox="0 0 82 82" width="82" height="82">
            <circle cx="41" cy="41" r="40" fill="var(--grey-pie)"/>
            <path d="M41 41 L41 1 A40 40 0 0 1 75.6 61 Z" fill="url(#sun)"/>
          </svg>
          <div class="product-copy">
            <h4>Mo-Fr von 9:00-17:00 Uhr</h4>
            <p>Gute Erreichbarkeit ist die Basis für professionellen Kundenservice. Als Visitenkarte für Ihr Unternehmen sorgen wir dafür dass Sie keinen Anruf mehr verpassen</p>
          </div>
        </div>
      </article>
      <article class="product">
        <div class="product-title">Erweiterte Bürozeiten</div>
        <div class="product-body">
          <svg viewBox="0 0 82 82" width="82" height="82">
            <circle cx="41" cy="41" r="40" fill="var(--grey-pie)"/>
            <path d="M41 41 L41 1 A40 40 0 1 1 20.3 75.2 Z" fill="url(#sun)"/>
          </svg>
          <div class="product-copy">
            <h4>Mo-Sa von 7:00-21:00 Uhr</h4>
            <p>Sie wollen für Ihre Kunden auch abends und am Wochenende erreichbar sein? Mit unseren Erweiterten Bürozeiten helfen wir Ihnen optimal!</p>
          </div>
        </div>
      </article>
      <article class="product">
        <div class="product-title">Rund um die Uhr</div>
        <div class="product-body">
          <svg viewBox="0 0 82 82" width="82" height="82">
            <circle cx="41" cy="41" r="40" fill="url(#sun)"/>
          </svg>
          <div class="product-copy">
            <h4>Mo-Sa von 0:00-24:00 Uhr</h4>
            <p>Sie wollen für Ihre Kunden auch abends und am Wochenende erreichbar sein? Mit unseren Erweiterten Bürozeiten helfen wir Ihnen optimal!</p>
          </div>
        </div>
      </article>
    </section>

    <div class="section-band">ADD ON'S</div>

    <section class="addons">
      <article class="addon">
        <div class="addon-title">Online Wissensdatenbank</div>
        <div class="addon-body">Unsere Online Wissensdatenbank stellt die Grundlage für die professionelle Sammlung Ihrer Informationen dar und dient als Schnittstelle zwischen Ihren Experten, CallCenter und Kunden. Strukturierte Informationsaufbereitung ermöglicht Suchanfragen nach Stichworten, Kategorien und/oder Freitext.</div>
      </article>
      <article class="addon">
        <div class="addon-title">Online Terminkalender</div>
        <div class="addon-body">Sämtliche Anforderungen wie Terminlängen, Kategorien, Zeitfenster,etc. werden individuell an Ihre Bedürfnisse angepasst und ermöglichen ortsunabhängig alle Termine zu verwalten. Eine Tages- oder Wochenansicht bietet zusätzlich einen strukturierten Gesamtüberblick aller Termine.</div>
      </article>
      <article class="addon">
        <div class="addon-title">Tonbänder &amp; Co</div>
        <div class="addon-body">Sie haben die Möglichkeit mit neutralen und individuellen Bandansagen oder einer Anrufbeantworterfunktion Ihren Kunden noch mehr Service zu bieten.</div>
      </article>
    </section>
  </main>
</body>
</html>
```